Business Card

We need a business card for a fundraising/sales and marketing company called Kelvora Appeals services. The logo colours are Red Black and white. The final design should communicate professional, reliable yet fun and charity minded
Updates

Sorry for the delay. A decision will be made in the next 48 hours. we are stuck between two designs. Kind Regards, Molly Ravenscroft

Industry/Entity Type

Marketing

```html
<!DOCTYPE html>
<html lang="en">
<head>
<meta charset="utf-8">
<title>Kelvora Appeals services – Business Card</title>
<link rel="stylesheet" href="https://fonts.googleapis.com/css2?family=Didact+Gothic&family=Montserrat:wght@700&display=swap">
<style>
  :root {
    --red: #e3232c;
    --ink: #3a3a3a;
    --grey: #555555;
    --paper: #ffffff;
    --backdrop: #e9e6e1;
  }
  html, body {
    margin: 0;
    width: 1200px;
    height: 903px;
    overflow: hidden;
    background: var(--backdrop);
  }
  .card {
    position: absolute;
    left: 180px;
    top: 211px;
    width: 840px;
    height: 480px;
    background: var(--paper);
    box-shadow: 0 10px 30px rgba(0,0,0,.18);
    font-family: "Didact Gothic", sans-serif;
    color: var(--ink);
    overflow: hidden;
  }
  .band { position: absolute; height: 22px; background: var(--red); }
  .band--top { top: 24px; left: 300px; right: 0; }
  .band--bottom { bottom: 24px; left: 0; width: 640px; }

  .brand {
    position: absolute;
    top: 72px;
    right: 40px;
    display: flex;
    align-items: center;
    gap: 14px;
    font-size: 52px;
    letter-spacing: 2px;
    color: var(--ink);
  }
  .brand__dot { width: 22px; height: 22px; background: var(--red); }

  .contact { position: absolute; left: 44px; top: 96px; width: 300px; }
  .contact__name {
    font-family: "Montserrat", sans-serif;
    font-weight: 700;
    font-size: 24px;
    color: var(--red);
    margin: 0;
  }
  .contact__name span { font-family: "Didact Gothic", sans-serif; font-weight: 400; color: var(--ink); }
  .contact__role { font-size: 15px; margin: 4px 0 18px; }
  .contact__rule { height: 2px; background: var(--red); width: 290px; margin-bottom: 24px; }
  .contact__list { list-style: none; margin: 0; padding: 0; font-size: 18px; }
  .contact__list li { display: flex; align-items: center; gap: 10px; margin-bottom: 10px; }
  .contact__list svg { width: 16px; height: 16px; flex: none; }

  .crowd {
    position: absolute;
    left: 370px;
    top: 210px;
    width: 360px;
    height: 210px;
    border-radius: 6px;
    background: linear-gradient(90deg, #555 0%, #555 18%, var(--red) 22%, var(--red) 40%, #555 44%, #555 100%);
    opacity: .85;
  }
</style>
</head>
<body>
  <article class="card">
    <div class="band band--top"></div>
    <div class="band band--bottom"></div>

    <div class="brand">
      <span class="brand__dot"></span>
      <span class="brand__name">KELVORA APPEALS</span>
    </div>

    <section class="contact">
      <h1 class="contact__name">DECLAN <span>HARTWELL</span></h1>
      <p class="contact__role">Managing Director</p>
      <div class="contact__rule"></div>
      <ul class="contact__list">
        <li>
          <svg viewBox="0 0 16 16" aria-hidden="true"><path fill="var(--red)" d="M3 1l3 3-2 2c1 2 3 4 5 5l2-2 3 3-2 3C6 15 1 10 1 3z"/></svg>
          0400 555 019
        </li>
        <li>
          <svg viewBox="0 0 16 16" aria-hidden="true"><rect x="1" y="3" width="14" height="10" fill="var(--red)"/><path d="M1 3l7 6 7-6" stroke="#fff" stroke-width="1.5" fill="none"/></svg>
          declan@kelvoraappeals.com
        </li>
        <li>
          <svg viewBox="0 0 16 16" aria-hidden="true"><circle cx="8" cy="8" r="6.5" stroke="var(--red)" stroke-width="2" fill="none"/><path d="M1.5 8h13M8 1.5c-3 3.5-3 9.5 0 13M8 1.5c3 3.5 3 9.5 0 13" stroke="var(--red)" stroke-width="1.2" fill="none"/></svg>
          www.kelvoraappeals.com
        </li>
      </ul>
    </section>

    <div class="crowd" role="img" aria-label="Silhouettes of a group of people standing in a row, one highlighted in red"></div>
  </article>
</body>
</html>
```